Executive retreat/workshop flyer for Keystone Passage

Our company, Keystone Passage, runs intensive week long residential retreats for executives suffering from burnout syndrome. We have a programme of therapy which will enable clients to get clarity on what they want out of life and how to achieve it.

Our website is www.keystonepassage.example. The flyer should have a consistent look and feel to the website. The flyer should be suitable for electronic distribution as well as printing.

The copy should read:

What is it all for? (IN BIG BOLD FONT)

We invite you to The Keystone Passage

Discover a more meaningful way of being in this world and put passion and purpose back into your life.

Our leading experts will guide you through a holistic program of intellectual, physical, emotional, spiritual and financial work.

You will:

- Draw up a vision of how you want to live your life
- Understand negative behavior loops and how to manage them
- Rebalance relationships which have suffered from stress and neglect
- Examine your attitudes towards money through the Octavial System
- Access practical advice on how to implement your goals

Please join us in the beautiful Tarrowby Peninsula this August for a life-changing journey.

This is an intensive program custom tailored to your individual needs. We can only take on a very limited number of participants to maintain intimacy and quality of attention. Book early to avoid disappointment.

Details:

date - mon 27 August - sat 1 sept 2012

Venue- kestrelwood Eco retreat, stony vale, Australia, 1 hour from Melbourne

Price- Special launch offer of US$ 13,860 which is a 30% discount off the normal price of US$ 19,800

10% of profits go to charity

All accommodation, food and individual consultations included.

Please email info@keystonepassage.example or contact Marnie at 9316 2047

Target Market(s)

Senior executives and leaders mostly with a financial background.

Industry/Entity Type

Residential

Requirements
Must have
• The brochure should look clear in electronic and print format. Can use photos which I've attached.
Nice to have
• Should have a warm, serene feel but appear professional and reliable.

```html
<!DOCTYPE html>
<html lang="en">
<head>
<meta charset="utf-8">
<title>What is it all for? – The Keystone Passage</title>
<link rel="stylesheet" href="https://fonts.googleapis.com/css2?family=Cinzel:wght@400;700&family=Arimo:ital,wght@0,400;0,700;1,400;1,700&display=swap">
<style>
  :root {
    --plum: #4e0a55;
    --plum-deep: #3d0744;
    --olive: #7f8f17;
    --ink: #111111;
    --paper: #ffffff;
    --cream: #f3f6df;
    --cream-light: #fbfcf3;
    --stage: #eef0ea;
    --leaf-gold: #c89a2c;
    --leaf-green: #5d7a2e;
    --leaf-red: #a8452a;
    --leaf-shade: #2f4a2a;
    --mist: rgba(232, 238, 214, 0.86);
  }
  * { box-sizing: border-box; margin: 0; padding: 0; }
  html, body {
    width: 1200px; height: 900px; overflow: hidden;
    background: var(--stage);
  }
  .flyer {
    position: absolute; left: 319px; top: 54px;
    width: 562px; height: 792px;
    background: var(--paper);
    border: 1px solid #9a9a9a;
    overflow: hidden;
    font-family: 'Arimo', Arial, sans-serif;
    color: var(--ink);
  }
  .hero-photo {
    position: absolute; left: 0; top: 0; width: 100%; height: 276px;
    background:
      radial-gradient(ellipse 120px 90px at 300px 150px, rgba(255,250,220,0.85), transparent 70%),
      radial-gradient(ellipse 160px 110px at 80px 70px, var(--leaf-red), transparent 75%),
      radial-gradient(ellipse 200px 120px at 460px 60px, var(--leaf-gold), transparent 75%),
      linear-gradient(180deg, var(--leaf-green) 0%, var(--leaf-shade) 55%, #6f8a4c 100%);
  }
  .hero-mist {
    position: absolute; left: 0; top: 176px; width: 100%; height: 100px;
    background: var(--mist);
  }
  .headline {
    position: absolute; left: 0; top: 6px; width: 100%;
    text-align: center;
    font-family: 'Cinzel', 'Times New Roman', serif;
    font-weight: 700; font-size: 82px; line-height: 0.86;
    color: var(--paper);
    -webkit-text-stroke: 2px var(--plum);
    paint-order: stroke fill;
    letter-spacing: 1px;
  }
  .invite {
    position: absolute; left: 0; top: 146px; width: 100%;
    text-align: center;
    font-weight: 700; font-style: italic; font-size: 24px;
    color: var(--paper);
    text-shadow: 0 1px 2px rgba(0,0,0,0.45);
  }
  .brand {
    position: absolute; left: 0; top: 186px; width: 100%;
    text-align: center;
  }
  .brand-dot {
    display: block; margin: 0 auto 14px;
    width: 40px; height: 40px; border-radius: 50%;
    background: var(--plum);
  }
  .brand-name {
    font-family: 'Cinzel', 'Times New Roman', serif;
    font-weight: 400; font-size: 26px; letter-spacing: 0.5px;
    color: var(--olive);
  }
  .rule { position: absolute; left: 0; top: 275px; width: 100%; height: 2px; background: var(--plum); }
  .lead {
    position: absolute; left: 30px; right: 30px; top: 290px;
    text-align: center;
    font-family: 'Cinzel', 'Times New Roman', serif;
    font-weight: 700; font-size: 18.5px; line-height: 24px;
    color: var(--plum);
  }
  .promise {
    position: absolute; left: 24px; right: 24px; top: 372px;
    text-align: center;
    font-weight: 700; font-size: 15.5px; line-height: 23px;
    color: var(--olive);
  }
  .col-title {
    font-family: 'Cinzel', 'Times New Roman', serif;
    font-weight: 700; font-size: 13px; line-height: 20px;
    color: var(--olive); letter-spacing: 0.3px;
  }
  .outcomes { position: absolute; left: 34px; width: 230px; top: 427px; }
  .outcomes ul { list-style: none; margin-top: 0; }
  .outcomes li {
    position: relative; padding-left: 12px;
    font-size: 11.2px; line-height: 15.5px; margin-bottom: 3.5px;
  }
  .tick { position: absolute; left: 0; top: 3px; width: 10px; height: 9px; }
  .invitation { position: absolute; left: 300px; width: 240px; top: 427px; }
  .invitation .col-title { line-height: 22px; }
  .invitation p {
    margin-top: 12px;
    font-size: 11.2px; line-height: 17px;
  }
  .details-band {
    position: absolute; left: 0; top: 621px; width: 100%; height: 20px;
    background: var(--plum-deep);
    color: var(--paper);
    text-align: center;
    font-weight: 700; font-size: 15px; line-height: 20px; letter-spacing: 2px;
  }
  .details {
    position: absolute; left: 0; top: 641px; width: 100%; height: 151px;
    background: linear-gradient(180deg, var(--cream-light), var(--cream));
  }
  .detail-col { position: absolute; top: 6px; }
  .detail-col.when { left: 34px; width: 240px; }
  .detail-col.cost { left: 299px; width: 230px; }
  .label { font-style: italic; font-size: 13px; line-height: 15px; }
  .value { font-weight: 700; font-size: 12.6px; line-height: 15px; margin-bottom: 6px; }
  .fine {
    position: absolute; left: 0; top: 99px; width: 100%;
    text-align: center; font-size: 10.6px; line-height: 17px;
  }
</style>
</head>
<body>
  <article class="flyer">
    <div class="hero-photo" role="img" aria-label="Sunlit autumn leaves over a garden path at the retreat"></div>
    <div class="hero-mist"></div>
    <h1 class="headline">What is it<br>all for?</h1>
    <p class="invite">We invite you to:</p>
    <div class="brand">
      <span class="brand-dot"></span>
      <span class="brand-name">The Keystone Passage</span>
    </div>
    <div class="rule"></div>

    <h2 class="lead">Discover a more meaningful way of being in this world and put passion and purpose back into your life.</h2>
    <p class="promise">Our leading experts will guide you through a holistic program of intellectual, physical, emotional, spiritual and financial work.</p>

    <section class="outcomes">
      <h3 class="col-title">You will:</h3>
      <ul>
        <li><svg class="tick" viewBox="0 0 10 9"><path d="M1 5 L4 8 L9 1" fill="none" stroke="#7f8f17" stroke-width="2"/></svg>Draw up a vision of how you want to live your life</li>
        <li><svg class="tick" viewBox="0 0 10 9"><path d="M1 5 L4 8 L9 1" fill="none" stroke="#7f8f17" stroke-width="2"/></svg>Understand negative behavior loops and how to manage them</li>
        <li><svg class="tick" viewBox="0 0 10 9"><path d="M1 5 L4 8 L9 1" fill="none" stroke="#7f8f17" stroke-width="2"/></svg>Rebalance relationships which have suffered from stress and neglect</li>
        <li><svg class="tick" viewBox="0 0 10 9"><path d="M1 5 L4 8 L9 1" fill="none" stroke="#7f8f17" stroke-width="2"/></svg>Examine your attitudes towards money through the Octavial System</li>
        <li><svg class="tick" viewBox="0 0 10 9"><path d="M1 5 L4 8 L9 1" fill="none" stroke="#7f8f17" stroke-width="2"/></svg>Access practical advice on how to implement your goals</li>
      </ul>
    </section>

    <section class="invitation">
      <h3 class="col-title">Please join us in the beautiful Tarrowby Peninsula this August for a life-changing journey.</h3>
      <p>This is an intensive program custom tailored to your individual needs. We can only take on a very limited number of participants to maintain intimacy and quality of attention. Book early to avoid disappointment.</p>
    </section>

    <div class="details-band">Details</div>
    <section class="details">
      <div class="detail-col when">
        <p class="label">Date:</p>
        <p class="value">Mon 27 August - Sat 1 sept 2012</p>
        <p class="label">Venue:</p>
        <p class="value">Kestrelwood Eco Retreat, stony vale, Australia, 1 hour from Melbourne</p>
      </div>
      <div class="detail-col cost">
        <p class="label">Price:</p>
        <p class="value">Special launch offer of US$ 13,860 which is a 30% discount off the normal price of US$ 19,800 10% of profits go to charity</p>
      </div>
      <p class="fine">All accommodation, food and individual consultations included.<br>Please email info@keystonepassage.example or contact Marnie at 9316 2047</p>
    </section>
  </article>
</body>
</html>
```